Looking for an attractive, cool poster design for our company Core Values. This would ideally be framed and placed at each company location. Would like this to be striking and memorable.

The core values that should be included on the poster are:

Be a Creator
Have an Open Mind
Do the Right Thing

The size should be standard poster size, 18 x 24, vertical orientation ideally.

The company name to include on the poster is:

Brightwater Systems Group

The design could be printed as a poster or a sticker/decal as well. Or perhaps printed on a fabric, foam boards. Versatile enough design for different output types.

Target Market(s)

Internal Team Members and visitors

Industry/Entity Type

Technology

Font styles to use
Other font styles liked:
• Montserrat

Requirements
Must have
• The design could be printed as a poster or a sticker/decal as well. Or perhaps printed on a fabric. Versatile enough design for different output types.

```html
<!DOCTYPE html>
<html lang="en">
<head>
<meta charset="utf-8">
<title>Core Values Poster – Brightwater Systems Group</title>
<link rel="stylesheet" href="https://fonts.googleapis.com/css2?family=Montserrat:wght@800&family=Oswald:wght@500&display=swap">
<style>
  :root {
    --backdrop: #c9c9cb;
    --paper: #e6e2dc;
    --navy: #0e4a6f;
    --orange: #d2762e;
  }
  html, body {
    margin: 0;
    padding: 0;
    width: 1200px;
    height: 559px;
    overflow: hidden;
    background: var(--backdrop);
  }
  .poster-sheet { display: block; }
  .poster-panel { fill: var(--paper); }
  .title-vertical {
    font-family: "Montserrat", sans-serif;
    font-weight: 800;
    fill: var(--navy);
  }
  .divider { fill: var(--orange); }
  .value-lead, .value-key {
    font-family: "Oswald", sans-serif;
    font-weight: 500;
    font-size: 82px;
  }
  .value-lead { fill: var(--navy); }
  .value-key { fill: var(--orange); }
  .brand-name {
    font-family: "Montserrat", sans-serif;
    font-weight: 800;
    fill: var(--navy);
  }
  .brand-dot { fill: var(--orange); }
</style>
</head>
<body>
<svg class="poster-sheet" width="1200" height="559" viewBox="0 0 2576 1200" xmlns="http://www.w3.org/2000/svg" role="img" aria-label="Three layout versions of the Brightwater Systems Group core values poster">

  <!-- Version A: name beside dot, centred -->
  <g class="poster poster-a">
    <rect class="poster-panel" x="160" y="136" width="655" height="884"/>
    <text class="title-vertical" transform="translate(315 860) rotate(-90)" font-size="112" textLength="645" lengthAdjust="spacingAndGlyphs">CORE VALUES</text>
    <rect class="divider" x="329" y="210" width="8" height="647" rx="4"/>
    <text class="value-lead" x="358" y="275" textLength="134" lengthAdjust="spacingAndGlyphs">BE A</text>
    <text class="value-key" x="358" y="370" textLength="274" lengthAdjust="spacingAndGlyphs">CREATOR</text>
    <text class="value-lead" x="358" y="517" textLength="257" lengthAdjust="spacingAndGlyphs">HAVE AN</text>
    <text class="value-key" x="358" y="610" textLength="337" lengthAdjust="spacingAndGlyphs">OPEN MIND</text>
    <text class="value-lead" x="358" y="763" textLength="217" lengthAdjust="spacingAndGlyphs">DO THE</text>
    <text class="value-key" x="358" y="857" textLength="390" lengthAdjust="spacingAndGlyphs">RIGHT THING</text>
    <circle class="brand-dot" cx="362" cy="974" r="24"/>
    <text class="brand-name" x="400" y="977" font-size="30" textLength="238" lengthAdjust="spacingAndGlyphs">BRIGHTWATER</text>
    <text class="brand-name" x="400" y="997" font-size="18" textLength="238" lengthAdjust="spacingAndGlyphs">SYSTEMS GROUP</text>
  </g>

  <!-- Version B: stacked name, bottom right -->
  <g class="poster poster-b">
    <rect class="poster-panel" x="961" y="136" width="655" height="884"/>
    <text class="title-vertical" transform="translate(1112 830) rotate(-90)" font-size="108" textLength="650" lengthAdjust="spacingAndGlyphs">CORE VALUES</text>
    <rect class="divider" x="1129" y="182" width="8" height="645" rx="4"/>
    <text class="value-lead" x="1160" y="245" textLength="133" lengthAdjust="spacingAndGlyphs">BE A</text>
    <text class="value-key" x="1160" y="340" textLength="272" lengthAdjust="spacingAndGlyphs">CREATOR</text>
    <text class="value-lead" x="1160" y="490" textLength="255" lengthAdjust="spacingAndGlyphs">HAVE AN</text>
    <text class="value-key" x="1160" y="580" textLength="335" lengthAdjust="spacingAndGlyphs">OPEN MIND</text>
    <text class="value-lead" x="1160" y="735" textLength="216" lengthAdjust="spacingAndGlyphs">DO THE</text>
    <text class="value-key" x="1160" y="828" textLength="388" lengthAdjust="spacingAndGlyphs">RIGHT THING</text>
    <circle class="brand-dot" cx="1497" cy="930" r="26"/>
    <text class="brand-name" x="1497" y="982" font-size="26" text-anchor="middle" textLength="184" lengthAdjust="spacingAndGlyphs">BRIGHTWATER</text>
    <text class="brand-name" x="1497" y="998" font-size="15" text-anchor="middle" textLength="184" lengthAdjust="spacingAndGlyphs">SYSTEMS GROUP</text>
  </g>

  <!-- Version C: larger name beside dot -->
  <g class="poster poster-c">
    <rect class="poster-panel" x="1761" y="136" width="655" height="884"/>
    <text class="title-vertical" transform="translate(1915 860) rotate(-90)" font-size="112" textLength="645" lengthAdjust="spacingAndGlyphs">CORE VALUES</text>
    <rect class="divider" x="1929" y="210" width="8" height="647" rx="4"/>
    <text class="value-lead" x="1958" y="275" textLength="134" lengthAdjust="spacingAndGlyphs">BE A</text>
    <text class="value-key" x="1958" y="370" textLength="274" lengthAdjust="spacingAndGlyphs">CREATOR</text>
    <text class="value-lead" x="1958" y="517" textLength="257" lengthAdjust="spacingAndGlyphs">HAVE AN</text>
    <text class="value-key" x="1958" y="610" textLength="337" lengthAdjust="spacingAndGlyphs">OPEN MIND</text>
    <text class="value-lead" x="1958" y="763" textLength="217" lengthAdjust="spacingAndGlyphs">DO THE</text>
    <text class="value-key" x="1958" y="857" textLength="390" lengthAdjust="spacingAndGlyphs">RIGHT THING</text>
    <circle class="brand-dot" cx="1942" cy="968" r="30"/>
    <text class="brand-name" x="1985" y="972" font-size="36" textLength="280" lengthAdjust="spacingAndGlyphs">BRIGHTWATER</text>
    <text class="brand-name" x="1985" y="995" font-size="21" textLength="280" lengthAdjust="spacingAndGlyphs">SYSTEMS GROUP</text>
  </g>
</svg>
</body>
</html>
```